card design for engineering consultancy

engineering drafting and project management company the provides drafting services for.
Electrical, Hydraulic, Mechanical, and Civil services
The company is called Q7R Services and logo is as attached
Information on card should be.
1. Logo
2.website : Q7RServices.example
3. email : info@Q7RServices.example
4. Phone: (+61) 400512836
5. Motto: Design - Document - Develop - Deliver

this card should be basically used for business identification only

Target Market(s)

electricians plumbers air conditioning installers and civil contractors

Industry/Entity Type

engineering, drafting, electrical, plumbing, airconditioning, civil

Contact Information for Business Card

1. Logo 2.website : Q7RServices.example 3. email : info@Q7RServices.example 4. Phone: (+61) 400512836 5. Motto: Design - Document - Develop - Deliver

Font styles to use
Serif

Requirements
Must have
• logo
Nice to have
• something inovative and different that makes it stand out from being just another business card

```html
<!DOCTYPE html>
<html lang="en">
<head>
<meta charset="utf-8">
<title>Q7R Services – Business Card</title>
<link rel="stylesheet" href="https://fonts.googleapis.com/css2?family=Michroma&family=Arimo:wght@400&display=swap">
<style>
  :root {
    --backdrop: #2a2b2e;
    --card: #1b1c20;
    --card-edge: #26272c;
    --silver: #c9cacd;
    --silver-dim: #a9abaf;
    --rule: #b7b8bc;
  }
  * { margin: 0; padding: 0; box-sizing: border-box; }
  html, body {
    width: 960px;
    height: 1200px;
    overflow: hidden;
    background: var(--backdrop);
  }
  .canvas {
    width: 960px;
    height: 1200px;
    display: flex;
    flex-direction: column;
    align-items: center;
    justify-content: center;
    gap: 80px;
  }
  .card {
    position: relative;
    width: 760px;
    height: 434px;
    background: var(--card);
    border: 1px solid var(--card-edge);
    box-shadow: 0 14px 34px rgba(0,0,0,0.45);
    color: var(--silver);
  }

  /* Front */
  .card--front {
    display: flex;
    align-items: center;
    justify-content: center;
  }
  .wordmark {
    display: flex;
    align-items: center;
    gap: 22px;
    font-family: "Michroma", sans-serif;
    color: var(--silver);
    text-transform: uppercase;
    letter-spacing: 0.08em;
  }
  .wordmark__square {
    background: var(--silver);
  }
  .card--front .wordmark { font-size: 40px; }
  .card--front .wordmark__square { width: 34px; height: 34px; }

  /* Back */
  .company-name {
    position: absolute;
    left: 86px;
    top: 58px;
    font-family: "Michroma", sans-serif;
    font-size: 27px;
    letter-spacing: 0.06em;
    text-transform: uppercase;
    color: var(--silver-dim);
  }
  .contact-list {
    position: absolute;
    left: 88px;
    top: 126px;
    list-style: none;
    font-family: "Arimo", sans-serif;
    font-size: 22px;
    color: var(--silver);
  }
  .contact-list li {
    display: flex;
    align-items: center;
    gap: 18px;
    height: 52px;
  }
  .contact-list svg { width: 22px; height: 22px; flex: none; }
  .card--back .wordmark {
    position: absolute;
    right: 40px;
    top: 98px;
    font-size: 20px;
    gap: 12px;
  }
  .card--back .wordmark__square { width: 18px; height: 18px; }
  .divider {
    position: absolute;
    left: 0;
    right: 0;
    top: 326px;
    height: 2px;
    background: var(--rule);
  }
  .motto {
    position: absolute;
    left: 0;
    right: 0;
    top: 360px;
    text-align: center;
    font-family: "Arimo", sans-serif;
    font-size: 23px;
    letter-spacing: 0.05em;
    text-transform: uppercase;
    color: var(--silver);
  }
</style>
</head>
<body>
<main class="canvas">

  <section class="card card--front" aria-label="Card front">
    <div class="wordmark">
      <span class="wordmark__square" aria-hidden="true"></span>
      <span class="wordmark__name">Q7R Services</span>
    </div>
  </section>

  <section class="card card--back" aria-label="Card back">
    <h1 class="company-name">Q7R Services</h1>

    <ul class="contact-list">
      <li>
        <svg viewBox="0 0 24 24" aria-hidden="true">
          <path fill="#c9cacd" d="M6.6 10.8a15.1 15.1 0 0 0 6.6 6.6l2.2-2.2a1 1 0 0 1 1-.25 11.4 11.4 0 0 0 3.6.57 1 1 0 0 1 1 1V20a1 1 0 0 1-1 1A17 17 0 0 1 3 4a1 1 0 0 1 1-1h3.5a1 1 0 0 1 1 1c0 1.25.2 2.45.57 3.57a1 1 0 0 1-.25 1z"/>
        </svg>
        <span>(+61) 400512836</span>
      </li>
      <li>
        <svg viewBox="0 0 24 24" aria-hidden="true">
          <rect x="2.5" y="5" width="19" height="14" fill="none" stroke="#c9cacd" stroke-width="1.8"/>
          <path d="M2.5 5l9.5 8 9.5-8M2.5 19l7-6.5M21.5 19l-7-6.5" fill="none" stroke="#c9cacd" stroke-width="1.6"/>
        </svg>
        <span>info@Q7RServices.example</span>
      </li>
      <li>
        <svg viewBox="0 0 24 24" aria-hidden="true">
          <circle cx="12" cy="12" r="9.5" fill="#c9cacd"/>
          <path d="M2.5 12h19M12 2.5c3 3 3 16 0 19M12 2.5c-3 3-3 16 0 19M4.5 7h15M4.5 17h15" fill="none" stroke="#1b1c20" stroke-width="1.2"/>
        </svg>
        <span>www.Q7RServices.example</span>
      </li>
    </ul>

    <div class="wordmark">
      <span class="wordmark__square" aria-hidden="true"></span>
      <span class="wordmark__name">Q7R Services</span>
    </div>

    <div class="divider" aria-hidden="true"></div>
    <p class="motto">Design - Document - Develop - Deliver</p>
  </section>

</main>
</body>
</html>
```